Sumvera financial services stationery design

We need business stationery designed with letterheads, business cards, with compliments and envelope for a business that offers tax and accounting services
Updates

Designs look the same

Target Market(s)

Small to medium businesses, individuals, Self managed superfunds

Industry/Entity Type

Business

Font styles to use
Serif
Other font styles liked:
• Atlanta

Colors
32a6d6
3277b5

Requirements
Must have
• Logo incorporated with all my stationery
• professional
Should not have
• Lots of colours
• Busy

```html
<!DOCTYPE html>
<html lang="en">
<head>
<meta charset="utf-8">
<title>Sumvera Financial Services – Stationery</title>
<link rel="stylesheet" href="https://fonts.googleapis.com/css2?family=Cinzel:wght@400;600&family=Arimo:wght@400;700&family=Questrial&display=swap">
<style>
:root{
  --stage:#4a4a4a;
  --paper:#ffffff;
  --blue:#2f77bb;
  --sky:#32a6d6;
  --ink:#555659;
  --text:#333333;
  --muted:#6a6a6a;
  --rule:#b9cde6;
}
*{box-sizing:border-box;margin:0;padding:0}
html,body{width:1000px;height:1200px;overflow:hidden}
body{background:var(--stage);position:relative;font-family:"Arimo",Arial,sans-serif;color:var(--text)}
.piece{position:absolute;background:var(--paper);overflow:hidden}
.abs{position:absolute}
.brand-name{font-family:"Cinzel",Georgia,serif;font-weight:400;color:var(--ink);line-height:1;white-space:nowrap}
.brand-tag{font-family:"Cinzel",Georgia,serif;color:var(--ink);line-height:1;white-space:nowrap}
.brand-square{position:absolute;background:var(--blue);border-radius:3px}
.contact{position:absolute;font-size:8px;line-height:1;white-space:nowrap;color:var(--text)}
.contact svg{width:8px;height:8px;vertical-align:-1px;margin-right:5px;fill:var(--blue)}
.address{position:absolute;text-align:right;font-size:8px;line-height:14px;white-space:nowrap}

/* cover */
.cover{left:47px;top:55px;width:400px;height:567px}
.cover-band{left:0;top:167px;width:400px;height:161px;background:var(--blue)}
.cover-square{left:132px;top:178px;width:136px;height:138px;background:var(--paper);border-radius:12px}
.cover .brand-name{left:0;width:400px;text-align:center;top:362px;font-size:74px;letter-spacing:1px}
.cover .brand-tag{left:0;width:400px;text-align:center;top:446px;font-size:21px;letter-spacing:4px}
.cover-url{left:0;top:512px;width:400px;height:31px;background:var(--blue);color:#fff;font-family:"Questrial",sans-serif;font-size:20px;letter-spacing:1.5px;text-align:center;line-height:31px}

/* letterhead */
.letterhead{left:548px;top:55px;width:401px;height:567px}
.letterhead-stripe{left:0;top:0;width:7px;height:567px;background:var(--blue)}
.letterhead .brand-square{left:45px;top:35px;width:16px;height:32px}
.letterhead .brand-name{left:22px;top:72px;font-size:20px}
.letterhead .brand-tag{left:23px;top:91px;font-size:5.5px;letter-spacing:1px}
.letterhead-contacts{left:278px;top:43px;height:49px;border-left:1.5px solid var(--blue)}
.letterhead-contacts .contact{left:6px;font-size:7.5px}
.salutation{left:24px;top:140px;font-size:8px;font-weight:700}
.letter-body{left:24px;top:157px;width:362px;font-size:5.9px;line-height:9.2px;color:#3a3a3a;text-align:justify}
.letter-body p{margin-bottom:10px}
.signoff{left:24px;top:463px;font-size:7px;line-height:1}
.signature{left:30px;top:475px;width:34px;height:10px}
.signer{left:24px;top:488px;font-size:5.5px;font-weight:700;line-height:7px}
.signer span{display:block;font-weight:400}
.letterhead-footer{left:24px;top:540px;width:362px;height:15px;background:var(--blue);color:#fff;font-size:8px;font-weight:700;letter-spacing:1px;text-align:center;line-height:15px}

/* compliments card */
.comp{left:13px;top:670px;width:468px;height:207px}
.comp .brand-square{left:37px;top:14px;width:20px;height:32px}
.comp .brand-name{left:13px;top:50px;font-size:22px}
.comp .brand-tag{left:15px;top:71px;font-size:6px;letter-spacing:1px}
.comp-line{left:0;top:200px;width:468px;height:7px;background:var(--blue)}

/* envelope */
.envelope{left:515px;top:670px;width:468px;height:207px}
.envelope svg.flap{position:absolute;left:0;top:0}
.envelope-square{left:211px;top:19px;width:46px;height:46px;background:var(--paper);border-radius:5px}
.envelope .brand-name{right:15px;top:161px;font-size:22px}
.envelope .brand-tag{right:15px;top:181px;font-size:6px;letter-spacing:1px}

/* card back */
.card-back{left:69px;top:928px;width:358px;height:204px;background:var(--blue);border-radius:18px}
.card-back-square{left:139px;top:29px;width:79px;height:77px;background:var(--paper);border-radius:6px}
.card-back .brand-name{left:0;width:358px;text-align:center;top:120px;font-size:44px;color:#fff}
.card-back .brand-tag{left:0;width:358px;text-align:center;top:166px;font-size:13px;letter-spacing:2px;color:#fff}

/* card front */
.card-front{left:571px;top:928px;width:358px;height:204px;border-radius:18px}
.card-front .brand-square{left:37px;top:8px;width:24px;height:40px}
.card-front .brand-name{left:7px;top:55px;font-size:25px}
.card-front .brand-tag{left:9px;top:79px;font-size:7.5px;letter-spacing:1.2px}
.holder-name{right:11px;top:105px;font-size:14px;font-weight:700;letter-spacing:1.5px;color:var(--blue);line-height:1}
.holder-role{right:11px;top:121px;font-size:9px;letter-spacing:2px;color:var(--muted);line-height:1}
.card-rule{left:0;top:137px;width:358px;height:1px;background:var(--rule)}
.card-front .contact{left:15px;font-size:10px}
.card-front .contact svg{width:10px;height:10px}
.card-front .address{right:11px;top:158px;font-size:10px;line-height:13px}
.card-front-band{left:0;top:192px;width:358px;height:12px;background:var(--blue)}
</style>
</head>
<body>

<svg width="0" height="0" style="position:absolute">
  <defs>
    <symbol id="icon-phone" viewBox="0 0 10 10"><path d="M1 3.5C1 2 2.5 1 5 1s4 1 4 2.5L7.5 4 7 3H3L2.5 4zM2.5 5h5l1 4h-7z"/></symbol>
    <symbol id="icon-mail" viewBox="0 0 10 10"><path d="M0 2h10v6H0z"/><path d="M0 2l5 3.5L10 2" stroke="#fff" stroke-width="1" fill="none"/></symbol>
    <symbol id="icon-web" viewBox="0 0 10 10"><circle cx="5" cy="5" r="4.5"/></symbol>
  </defs>
</svg>

<!-- Cover / folder -->
<section class="piece cover">
  <div class="abs cover-band"></div>
  <div class="abs cover-square"></div>
  <div class="abs brand-name">Sumvera</div>
  <div class="abs brand-tag">Financial Services</div>
  <div class="abs cover-url">www.sumveraservices.com</div>
</section>

<!-- Letterhead -->
<section class="piece letterhead">
  <div class="abs letterhead-stripe"></div>
  <div class="brand-square"></div>
  <div class="abs brand-name">Sumvera</div>
  <div class="abs brand-tag">Financial Services</div>
  <div class="abs letterhead-contacts">
    <div class="contact" style="top:5px"><svg><use href="#icon-phone"/></svg>(01) 2345 6789</div>
    <div class="contact" style="top:18px"><svg><use href="#icon-mail"/></svg>info@sumveraservices.com</div>
    <div class="contact" style="top:31px"><svg><use href="#icon-web"/></svg>www.sumveraservices.com</div>
  </div>
  <div class="abs salutation">Dear Mr. ABCD</div>
  <div class="abs letter-body">
    <p>Lorem Ipsum is simply dummy text of the printing and typesetting industry. Lorem Ipsum has been the industry's standard dummy text ever since the 1500s, when an unknown printer took a galley of type and scrambled it to make a type specimen book. It has survived not only five centuries, but also the leap into electronic typesetting, remaining essentially unchanged. It was popularised in the 1960s with the release of transfer sheets containing Lorem Ipsum passages, and more recently with desktop layout software including versions of Lorem Ipsum.</p>
    <p>Contrary to popular belief, Lorem Ipsum is not simply random text. It has roots in a piece of classical Latin literature from 45 BC, making it over 2000 years old. A Latin professor looked up one of the more obscure Latin words, consectetur, from a Lorem Ipsum passage, and going through the cites of the word in classical literature, discovered the undoubtable source. Lorem Ipsum comes from sections 1.10.32 and 1.10.33 of an old treatise on the extremes of good and evil by a Roman writer, written in 45 BC. This book is a treatise on the theory of ethics, very popular during the Renaissance. The first line of Lorem Ipsum, "Lorem ipsum dolor sit amet..", comes from a line in section 1.10.32.</p>
    <p>The standard chunk of Lorem Ipsum used since the 1500s is reproduced below for those interested. Sections 1.10.32 and 1.10.33 from the same old treatise are also reproduced in their exact original form, accompanied by English versions from a later translator.</p>
    <p>It is a long established fact that a reader will be distracted by the readable content of a page when looking at its layout. The point of using Lorem Ipsum is that it has a more-or-less normal distribution of letters, as opposed to using 'Content here, content here', making it look like readable English. Many desktop publishing packages and web page editors now use Lorem Ipsum as their default model text, and a search for 'lorem ipsum' will uncover many web sites still in their infancy. Various versions have evolved over the years, sometimes by accident, sometimes on purpose (injected humour and the like).</p>
    <p>There are many variations of passages of Lorem Ipsum available, but the majority have suffered alteration in some form, by injected humour, or randomised words which don't look even slightly believable. If you are going to use a passage of Lorem Ipsum, you need to be sure there isn't anything embarrassing hidden in the middle of text. All the Lorem Ipsum generators on the Internet tend to repeat predefined chunks as necessary, making this the first true generator on the Internet. It uses a dictionary of over 200 Latin words, combined with a handful of model sentence structures, to generate Lorem Ipsum which looks reasonable. The generated Lorem Ipsum is therefore always free from repetition, injected humour, or non-characteristic words etc.</p>
  </div>
  <div class="abs signoff">Sincerely Yours,</div>
  <svg class="abs signature" viewBox="0 0 34 10" aria-hidden="true"><path d="M1 7c3-6 5-6 4 0s4-5 6-3 3 3 6 0 5 2 8 1" fill="none" stroke="#333" stroke-width="0.8"/></svg>
  <div class="abs signer">Dana Whitfield<span>Executive Director</span></div>
  <div class="abs letterhead-footer">PO BOX 123 your address, 2nd streed, USA.</div>
</section>

<!-- With compliments card -->
<section class="piece comp">
  <div class="brand-square"></div>
  <div class="abs brand-name">Sumvera</div>
  <div class="abs brand-tag">Financial Services</div>
  <div class="contact" style="left:12px;top:153px"><svg><use href="#icon-phone"/></svg>(01) 2345 6789</div>
  <div class="contact" style="left:12px;top:167px"><svg><use href="#icon-mail"/></svg>info@sumveraservices.com</div>
  <div class="contact" style="left:12px;top:181px"><svg><use href="#icon-web"/></svg>www.sumveraservices.com</div>
  <div class="address" style="right:11px;top:165px">PO BOX 123 your address<br>2nd streed, USA.</div>
  <div class="abs comp-line"></div>
</section>

<!-- Envelope -->
<section class="piece envelope">
  <svg class="flap" width="468" height="80" viewBox="0 0 468 80" aria-hidden="true">
    <path d="M0 0H468V52Q350 56 240 76Q232 77.5 226 76Q120 56 0 52Z" fill="var(--blue)"/>
  </svg>
  <div class="abs envelope-square"></div>
  <div class="abs brand-name">Sumvera</div>
  <div class="abs brand-tag">Financial Services</div>
</section>

<!-- Business card back -->
<section class="piece card-back">
  <div class="abs card-back-square"></div>
  <div class="abs brand-name">Sumvera</div>
  <div class="abs brand-tag">Financial Services</div>
</section>

<!-- Business card front -->
<section class="piece card-front">
  <div class="brand-square"></div>
  <div class="abs brand-name">Sumvera</div>
  <div class="abs brand-tag">Financial Services</div>
  <div class="abs holder-name">YOUR NAME</div>
  <div class="abs holder-role">DIRECTOR</div>
  <div class="abs card-rule"></div>
  <div class="contact" style="top:146px"><svg><use href="#icon-phone"/></svg>(01) 2345 6789</div>
  <div class="contact" style="top:159px"><svg><use href="#icon-mail"/></svg>info@sumveraservices.com</div>
  <div class="contact" style="top:171px"><svg><use href="#icon-web"/></svg>www.sumveraservices.com</div>
  <div class="address">PO BOX 123 your address<br>2nd streed, USA.</div>
  <div class="abs card-front-band"></div>
</section>

</body>
</html>
```